First Website for Meridian Advisory Collective

We need a great new website design to flow with our brand identity (attached; developed here on ArtHive just recently). It needs to be professional, but with just a little bit of fun thrown in, to reflect the caribbean location of our business. The logo already achieves this and thus it should flow from there.

The site will have a few primary sections:

Home - self explanatory, and overview of our business and some of the most recent posts from the next section
Notes - Really just a fancy word for a blog, it will be an ordered set of posts on various regulatory and business news items relevant to Caribbean businesses
"Start/Relocate a Consulting Practice?" or "Become a Partner" - A section on how to bring a consulting practice, new or old, into the partnership and the tax and regulatory advantages of doing so
Contact - Self explanatory

So, it needs a navigation that supports that sparse set of top level links, and a basic design for home, one interior page like "Become a Partner", and the blog/Notes section, that my developer can work from.

UPDATE: I like the designs that have brought in the logo colors to make each sub-page uniquely colored. But, all so far rely too heavily on smiling photos of people. 1) Notes will not have photos to go with them (this is going to be mostly legal updates, tax info, etc.) 2) For the hero photon on the home page, it shouldn't be too high, and should probably be a photo of a beach, preferably one from Puerto Rico where we are located. 3) There should be no search and no social media buttons - the design is meant to be sparse on purpose and we have no need for those items.

Other than the logo, please stick to web safe or google web fonts for text, and have them specified in the source format during delivery. Thanks.

Target Market(s)

Business owners. Often in high tech fields. As well as high net worth family offices.

Industry/Entity Type

Legal

Requirements
Must have
• Must pull in colors from the logo effectively, without looking garish or overly bright.

```html
<!DOCTYPE html>
<html lang="en">
<head>
<meta charset="utf-8">
<title>Meridian Advisory Collective — Home</title>
<link href="https://fonts.googleapis.com/css2?family=Open+Sans:wght@400;600&display=swap" rel="stylesheet">
<style>
  :root {
    --brand-red: #b5161c;
    --brand-red-dark: #8e0f13;
    --brand-red-text: #b0142a;
    --accent-green: #5a9e5e;
    --button-green: #5ea760;
    --link-blue: #3a82c4;
    --text-body: #555555;
    --text-muted: #888888;
    --rule: #dddddd;
    --panel-bg: #efefef;
    --panel-border: #d5d5d5;
    --footer-bg: #2e2e2e;
    --footer-text: #bdbdbd;
    --button-grey: #7d7d7d;
    --sea: #3f8fb0;
    --sand: #e6d7b5;
    --white: #ffffff;
  }
  * { margin: 0; padding: 0; box-sizing: border-box; }
  html, body { width: 836px; height: 1200px; overflow: hidden; }
  body { position: relative; background: var(--white); font-family: "Open Sans", Arial, sans-serif; color: var(--text-body); }
  .abs { position: absolute; }

  /* Header */
  .brand { left: 70px; top: 22px; display: flex; align-items: center; gap: 10px; }
  .brand-mark { width: 26px; height: 26px; background: var(--brand-red); }
  .brand-name { font-size: 21px; font-weight: 600; color: var(--brand-red-text); line-height: 1.1; width: 200px; }
  .contact-top { right: 70px; top: 22px; text-align: right; }
  .contact-top .label { font-size: 12px; color: var(--text-muted); }
  .contact-top .email { font-size: 13px; color: var(--brand-red-text); }

  /* Navigation */
  .nav { left: 0; top: 83px; width: 836px; height: 36px; background: linear-gradient(#c01b21, var(--brand-red) 60%, #a81319); }
  .nav ul { list-style: none; position: absolute; left: 69px; top: 0; display: flex; height: 36px; }
  .nav li { font-size: 11.5px; color: var(--white); line-height: 36px; padding: 0 18px; }
  .nav li.active { background: var(--brand-red-dark); }
  .nav li + li { margin-left: 4px; }

  /* Hero */
  .hero { left: 0; top: 119px; width: 836px; height: 300px; background: linear-gradient(180deg, #9fd0e8 0%, #cfe8f2 38%, var(--sea) 52%, #6fb6c9 66%, var(--sand) 80%, #d8c49b 100%); }
  .hero-caption { left: 519px; top: 117px; width: 247px; height: 66px; background: rgba(34,34,34,0.85); color: var(--white); font-size: 19px; font-weight: 600; text-align: right; padding: 7px 13px 0 0; line-height: 26px; }
  .hero-dots { left: 382px; top: 272px; width: 70px; height: 16px; background: rgba(30,30,30,0.8); border-radius: 8px; }
  .hero-dots i { position: absolute; top: 4px; width: 8px; height: 8px; border-radius: 50%; background: var(--white); }
  .hero-dots i.current { background: none; border: 1.5px solid var(--white); }

  /* Sections */
  .section-title { font-size: 16px; font-weight: 600; color: var(--accent-green); }
  .overview-title { left: 0; width: 836px; top: 450px; text-align: center; }
  .overview-text { left: 88px; width: 660px; top: 477px; text-align: center; font-size: 9.6px; line-height: 16px; }
  .rule { left: 69px; top: 570px; width: 698px; height: 1px; background: var(--rule); }

  .services-title { left: 76px; top: 600px; }
  .services-text { left: 76px; top: 628px; width: 330px; font-size: 9.6px; line-height: 16px; }
  .services-image { left: 76px; top: 705px; width: 325px; height: 190px; background: linear-gradient(135deg, #cfc3ab, #8a7b63 60%, #4e4336); }

  .btn { display: block; font-size: 9.5px; font-weight: 600; color: var(--white); text-align: center; border-radius: 2px; }
  .btn-grey { background: linear-gradient(#8c8c8c, var(--button-grey)); height: 23px; line-height: 23px; }
  .btn-read { left: 76px; top: 910px; width: 70px; }
  .btn-view { left: 433px; top: 910px; width: 56px; }

  .notes-title { left: 433px; top: 600px; }
  .note { left: 433px; width: 333px; }
  .note.one { top: 630px; }
  .note.two { top: 745px; padding-top: 16px; border-top: 1px solid var(--rule); }
  .note-link { font-size: 11.5px; color: var(--link-blue); line-height: 15px; }
  .note-date { font-size: 9.6px; margin-top: 5px; }
  .note-text { font-size: 9.6px; line-height: 15px; margin-top: 8px; }

  /* Partner panel */
  .partner { left: 69px; top: 962px; width: 698px; height: 110px; background: var(--panel-bg); border: 1px solid var(--panel-border); text-align: center; }
  .partner .section-title { font-size: 13px; margin-top: 15px; }
  .partner p { font-size: 9.6px; line-height: 15px; width: 440px; margin: 3px auto 0; }
  .btn-register { background: var(--button-green); width: 86px; height: 22px; line-height: 22px; margin: 10px auto 0; }

  /* Footer */
  .footer { left: 0; top: 1100px; width: 836px; height: 100px; background: var(--footer-bg); }
  .footer-links { position: absolute; left: 70px; top: 28px; font-size: 9.5px; color: var(--footer-text); }
  .footer-links .sep { margin: 0 8px; }
  .copyright { position: absolute; left: 70px; top: 56px; font-size: 9.5px; color: var(--footer-text); }
</style>
</head>
<body>
  <header>
    <div class="abs brand">
      <span class="brand-mark"></span>
      <span class="brand-name">Meridian Advisory Collective</span>
    </div>
    <div class="abs contact-top">
      <div class="label">Contact us</div>
      <div class="email">hello@meridianadvisory.example</div>
    </div>
  </header>

  <nav class="abs nav">
    <ul>
      <li class="active">HOME</li>
      <li>ABOUT US</li>
      <li>SERVICES</li>
      <li>PARTNERS</li>
      <li>BLOG</li>
      <li>CONTACT US</li>
    </ul>
  </nav>

  <section class="abs hero" role="img" aria-label="Hero photograph: sunlit Puerto Rico beach with turquoise sea and pale sand">
    <div class="abs hero-caption">START/RELOCATE A<br>CONSULTING PRACTICE?</div>
    <div class="abs hero-dots">
      <i class="current" style="left:10px"></i>
      <i style="left:25px"></i><i style="left:40px"></i><i style="left:55px"></i>
    </div>
  </section>

  <h2 class="abs section-title overview-title">OVERVIEW</h2>
  <p class="abs overview-text">Overview Maecenas lobortis erat eget rutrum auctor. Fusce lorem tortor, dapibus quis hendrerit sed, vulputate sit amet eros. Aenean blandit sit amet mi a pulvinar. Nam convallis erat vitae libero tempor blandit. Vivamus consectetur magna tempus, dictum lorem ut, aliquam ipsum. Phasellus eu vehicula lacus. Etiam hendrerit a lectus quis sodales. Suspendisse id rhoncus sapien. Donec rutrum metus ac lectus condimentum, id dictum nibh aliquet. Nulla facilisi. Mauris sit amet iaculis felis. Sed cursus dapibus accumsan.</p>
  <div class="abs rule"></div>

  <h2 class="abs section-title services-title">OUR SERVICES</h2>
  <p class="abs services-text">Nam convallis erat vitae libero tempor blandit. Vivamus consectetur magna tempus, dictum lorem ut, aliquam ipsum. Phasellus eu vehicula lacus. Etiam hendrerit a lectus quis sodales. Suspendisse id rhoncus sapien sapien consectetur egestas.</p>
  <div class="abs services-image" role="img" aria-label="Photograph: team of business people in front of a wall of sketched diagrams"></div>
  <span class="abs btn btn-grey btn-read">READ MORE</span>

  <h2 class="abs section-title notes-title">NOTES</h2>
  <article class="abs note one">
    <div class="note-link">Cum sociis natoque penatibus et magnis dis</div>
    <div class="note-date">March 21, 2014</div>
    <div class="note-text">Nam convallis erat vitae libero tempor blandit. Vivamus consectetur magna tempus, dictum lorem ut, aliquam ipsum.</div>
  </article>
  <article class="abs note two">
    <div class="note-link">Cum sociis natoque penatibus et magnis dis</div>
    <div class="note-date">March 21, 2014</div>
    <div class="note-text">Nam convallis erat vitae libero tempor blandit. Vivamus consectetur magna tempus, dictum lorem ut, aliquam ipsum.</div>
  </article>
  <span class="abs btn btn-grey btn-view">VIEW ALL</span>

  <section class="abs partner">
    <h2 class="section-title">BECOME A PARTNER</h2>
    <p>Donec rutrum metus ac lectus condimentum, id dictum nibh aliquet. Nulla facilisi. Mauris sit amet iaculis felis. Sed cursus dapibus accumsan.</p>
    <span class="btn btn-register">REGISTER NOW</span>
  </section>

  <footer class="abs footer">
    <div class="footer-links">Home<span class="sep">|</span>About us<span class="sep">|</span>Services<span class="sep">|</span>Partners<span class="sep">|</span>Blog<span class="sep">|</span>Contact us</div>
    <div class="copyright">Copyright &copy; 2014 &nbsp;Meridian Advisory Collective. &nbsp;All rights reserved.</div>
  </footer>
</body>
</html>
```